Flashy and colorful banner for an orange grower

Hi, I need a graphic for an advertising banner (80x200cm) to be placed next to the sales van. So far we have tried to highlight the naturalness of our products. With this banner we would like to highlight the ancient Sicilian tradition, with the typical decorations, I attach some photos as an example. We will sell our products far from Sicily, so I would like to exalt our origin.
We would like to dare with a colorful and amazing design, to capture the attention of passers-by.
It might be nice to insert or rework the decoration within our logo.
I would like to insert 4 of our offers inside the banner, only in the upper part, from the middle up.
The text is:
DAL CUORE DELLA SICILIA
ARANCIA TAROCCO
ALLA RINFUSA
5€ BORSA
DA SPREMERE
10€ CASSETTA
DA TAVOLA
15€ CASSETTA
SELEZIONE PREMIUM
20€ CASSETTA
Thanks for your time

```html
<!DOCTYPE html>
<html lang="it">
<head>
<meta charset="UTF-8">
<title>Soledoro Sicilia – Roll-up Arancia Tarocco</title>
<link rel="stylesheet" href="https://fonts.googleapis.com/css2?family=Poppins:wght@500;600;700;800&family=Abril+Fatface&display=swap">
<style>
  :root{
    --page:#e9e9e9;
    --white:#ffffff;
    --frame-yellow:#f7d21a;
    --frame-red:#e5423a;
    --frame-blue:#5b9bd5;
    --green:#1f7a3a;
    --leaf-green:#4cae3c;
    --orange:#ef7d1a;
    --orange-deep:#e2561c;
    --orange-light:#f6c36a;
    --badge-blue:#1f48b8;
    --badge-red:#d63a2f;
    --badge-green:#2e9b47;
    --price-yellow:#ffd400;
    --ink:#1e1e1e;
  }
  *{box-sizing:border-box;margin:0;padding:0}
  html,body{width:1200px;height:2708px;overflow:hidden;background:var(--page)}
  .rollup{
    position:absolute;left:100px;top:106px;width:1000px;height:2496px;
    overflow:hidden;box-shadow:0 10px 24px rgba(0,0,0,.25);
  }
  .rollup__pattern{
    position:absolute;inset:0;
    background:
      linear-gradient(90deg,var(--frame-yellow) 0,#f9e27a 30%,#f8a93a 50%,#f9e27a 70%,var(--frame-yellow) 100%);
  }
  .rollup__panel{
    position:absolute;left:82px;top:86px;width:836px;height:2410px;
    background:var(--white);border:7px solid var(--frame-yellow);border-bottom:none;
  }
  .brand{position:absolute;left:0;right:0;top:172px;text-align:center}
  .brand__dot{
    width:200px;height:200px;border-radius:50%;margin:0 auto;
    background:var(--orange);
  }
  .brand__name{
    margin-top:30px;font-family:'Poppins',sans-serif;font-weight:600;
    font-size:62px;line-height:1;letter-spacing:1px;color:var(--green);
  }
  .brand__tagline{
    margin-top:22px;font-family:'Poppins',sans-serif;font-weight:500;
    font-size:17px;letter-spacing:5px;color:var(--orange-deep);
  }
  .offer{position:absolute;width:352px;height:352px}
  .offer svg{width:100%;height:100%;display:block}
  .offer text{font-family:'Poppins',sans-serif;text-anchor:middle}
  .offer__label{font-weight:700;font-size:29px;fill:var(--ink)}
  .offer__price{font-weight:800;font-size:58px;fill:var(--price-yellow)}
  .offer__unit{font-weight:700;font-size:24px;fill:var(--white)}
  .offer--1{left:125px;top:557px}
  .offer--2{left:504px;top:557px}
  .offer--3{left:125px;top:945px}
  .offer--4{left:504px;top:945px}
  .headline{position:absolute;left:0;right:0;top:1380px;text-align:center}
  .headline__kicker{
    font-family:'Poppins',sans-serif;font-weight:600;font-size:42px;
    letter-spacing:12px;color:var(--ink);
  }
  .headline__line{
    font-family:'Abril Fatface',serif;font-size:132px;line-height:1;letter-spacing:3px;
  }
  .headline__line--green{color:var(--leaf-green);margin-top:8px}
  .headline__line--orange{color:var(--orange);margin-top:6px}
  .headline__variety{
    margin-top:24px;font-family:'Poppins',sans-serif;font-weight:600;font-size:42px;
    letter-spacing:14px;color:var(--ink);
  }
  .orange-slice{position:absolute;left:0;bottom:0;width:1000px;height:640px}
  .orange-slice svg{width:100%;height:100%;display:block}
</style>
</head>
<body>
  <main class="rollup">
    <div class="rollup__pattern" role="img" aria-label="Cornice decorativa in stile carretto siciliano, motivi gialli, rossi e azzurri"></div>
    <div class="rollup__panel"></div>

    <header class="brand">
      <div class="brand__dot"></div>
      <div class="brand__name">SOLEDORO SICILIA</div>
      <div class="brand__tagline">NATURALMENTE SICILIANA</div>
    </header>

    <section class="offers">
      <div class="offer offer--1">
        <svg viewBox="0 0 352 352">
          <defs><clipPath id="inner1"><circle cx="176" cy="176" r="112"/></clipPath></defs>
          <circle cx="176" cy="176" r="176" fill="var(--badge-blue)"/>
          <circle cx="176" cy="176" r="128" fill="var(--white)"/>
          <circle cx="176" cy="176" r="121" fill="none" stroke="var(--badge-green)" stroke-width="7"/>
          <g clip-path="url(#inner1)">
            <rect x="0" y="0" width="352" height="352" fill="var(--white)"/>
            <rect x="0" y="176" width="352" height="176" fill="var(--badge-red)"/>
          </g>
          <text class="offer__label" x="176" y="128">ALLA</text>
          <text class="offer__label" x="176" y="160">RINFUSA</text>
          <text class="offer__price" x="176" y="228">5€</text>
          <text class="offer__unit" x="176" y="264">BORSA</text>
        </svg>
      </div>
      <div class="offer offer--2">
        <svg viewBox="0 0 352 352">
          <defs><clipPath id="inner2"><circle cx="176" cy="176" r="112"/></clipPath></defs>
          <circle cx="176" cy="176" r="176" fill="var(--badge-red)"/>
          <circle cx="176" cy="176" r="128" fill="var(--white)"/>
          <circle cx="176" cy="176" r="121" fill="none" stroke="var(--badge-green)" stroke-width="7"/>
          <g clip-path="url(#inner2)">
            <rect x="0" y="0" width="352" height="352" fill="var(--white)"/>
            <rect x="0" y="176" width="352" height="176" fill="var(--badge-blue)"/>
          </g>
          <text class="offer__label" x="176" y="128">DA</text>
          <text class="offer__label" x="176" y="160">SPREMERE</text>
          <text class="offer__price" x="176" y="228">10€</text>
          <text class="offer__unit" x="176" y="264">CASSETTA</text>
        </svg>
      </div>
      <div class="offer offer--3">
        <svg viewBox="0 0 352 352">
          <defs><clipPath id="inner3"><circle cx="176" cy="176" r="112"/></clipPath></defs>
          <circle cx="176" cy="176" r="176" fill="var(--badge-red)"/>
          <circle cx="176" cy="176" r="128" fill="var(--white)"/>
          <circle cx="176" cy="176" r="121" fill="none" stroke="var(--badge-green)" stroke-width="7"/>
          <g clip-path="url(#inner3)">
            <rect x="0" y="0" width="352" height="352" fill="var(--white)"/>
            <rect x="0" y="176" width="352" height="176" fill="var(--badge-blue)"/>
          </g>
          <text class="offer__label" x="176" y="128">DA</text>
          <text class="offer__label" x="176" y="160">TAVOLA</text>
          <text class="offer__price" x="176" y="228">15€</text>
          <text class="offer__unit" x="176" y="264">CASSETTA</text>
        </svg>
      </div>
      <div class="offer offer--4">
        <svg viewBox="0 0 352 352">
          <defs><clipPath id="inner4"><circle cx="176" cy="176" r="112"/></clipPath></defs>
          <circle cx="176" cy="176" r="176" fill="var(--badge-blue)"/>
          <circle cx="176" cy="176" r="128" fill="var(--white)"/>
          <circle cx="176" cy="176" r="121" fill="none" stroke="var(--badge-green)" stroke-width="7"/>
          <g clip-path="url(#inner4)">
            <rect x="0" y="0" width="352" height="352" fill="var(--white)"/>
            <rect x="0" y="176" width="352" height="176" fill="var(--badge-red)"/>
          </g>
          <text class="offer__label" x="176" y="128">SELEZIONE</text>
          <text class="offer__label" x="176" y="160">PREMIUM</text>
          <text class="offer__price" x="176" y="228">20€</text>
          <text class="offer__unit" x="176" y="264">CASSETTA</text>
        </svg>
      </div>
    </section>

    <section class="headline">
      <div class="headline__kicker">DAL CUORE</div>
      <div class="headline__line headline__line--green">DELLA</div>
      <div class="headline__line headline__line--orange">SICILIA</div>
      <div class="headline__variety">ARANCIA TAROCCO</div>
    </section>

    <div class="orange-slice" role="img" aria-label="Grande fetta d'arancia decorata con motivi floreali siciliani">
      <svg viewBox="0 0 1000 640" preserveAspectRatio="none">
        <defs>
          <radialGradient id="slice" cx="50%" cy="100%" r="95%">
            <stop offset="0" stop-color="var(--orange-light)"/>
            <stop offset=".55" stop-color="var(--orange)"/>
            <stop offset="1" stop-color="var(--orange-deep)"/>
          </radialGradient>
        </defs>
        <path d="M0 260 Q500 -120 1000 260 L1000 640 L0 640 Z" fill="url(#slice)"/>
      </svg>
    </div>
  </main>
</body>
</html>
```